Brinford Vet Core Values

Brinford Veterinary Services is both a small and large animal practice so we mainly work with cats, dogs, and cows. We want the sign to reflect all three of those animals as well as elements of farm/country life like barns and tractors. We're located in a small town, less then 4,000 people, so we would like the design to have a rural look and feel. We want to use a "rustic" color palette, follow the link to see what we have in mind https://www.palomercoatings.example/homeowners/color/find-and-explore-colors/paint-colors-by-collection/lifestyle-collection/toasted-meadow.
The text we want have appear on the sign is listed below. We also want to C in compassionate, the A in Always, the R in Ready, the E in Expanding, and the S in Service to be bold and standout since they will spell out cares.
"Brinford Veterinary Services is committed to Compassionate and honest care for all patients and clients. This means we are Always efficient with our resources to pass the savings on to our clients. We are also Ready to help with the best medicine available while Expanding to help more of our practice’s families and farms. This is how we provide Service in abundance to all our clients so they are proud to send their family and friends to see us. Brinford Vet CARES."

```html
<!DOCTYPE html>
<html lang="en">
<head>
<meta charset="utf-8">
<title>Brinford Vet Core Values</title>
<link href="https://fonts.googleapis.com/css2?family=Arvo:wght@700&family=Roboto+Slab:wght@300&family=Bebas+Neue&display=swap" rel="stylesheet">
<style>
  :root {
    --canvas: #ebedec;
    --paper: #fbfbf9;
    --paper-shade: #f1f2f0;
    --green: #5fa26f;
    --red: #cf5149;
    --white: #ffffff;
  }
  html, body {
    margin: 0;
    width: 1200px;
    height: 1200px;
    overflow: hidden;
    background: var(--canvas);
  }
  .sign {
    display: block;
    width: 1200px;
    height: 1200px;
  }
  .paper { fill: url(#paperTone); }
  .rule { stroke: var(--green); stroke-width: 1.4; }
  .band { fill: var(--green); }
  .slab-bold { font-family: "Arvo", "Rockwell", serif; font-weight: 700; fill: var(--green); }
  .slab-light { font-family: "Roboto Slab", "Rockwell", serif; font-weight: 300; fill: var(--green); }
  .condensed { font-family: "Bebas Neue", "Oswald", sans-serif; fill: var(--green); }
  .on-band { fill: var(--white); }
  .initial { fill: var(--red); }
</style>
</head>
<body>
<svg class="sign" viewBox="0 0 992 992" role="img" aria-label="Brinford Vet core values sign">
  <defs>
    <linearGradient id="paperTone" x1="0" y1="0" x2="1" y2="1">
      <stop offset="0" stop-color="#fdfdfc"/>
      <stop offset="0.5" stop-color="#f7f8f6"/>
      <stop offset="1" stop-color="#fbfbfa"/>
    </linearGradient>
  </defs>

  <rect class="paper" x="241" y="70" width="510" height="850"/>

  <!-- header -->
  <rect class="band" x="278" y="93" width="440" height="31"/>
  <text class="slab-bold on-band" x="288" y="117" font-size="21" textLength="420" lengthAdjust="spacingAndGlyphs">BRINFORD VETERINARY SERVICES</text>

  <!-- commitment -->
  <text class="slab-bold" x="285" y="157" font-size="25" textLength="425" lengthAdjust="spacingAndGlyphs">IS COMMITTED TO <tspan class="initial">C</tspan>OMPASSIONATE</text>
  <text class="slab-light" x="285" y="195" font-size="42" textLength="425" lengthAdjust="spacingAndGlyphs">AND HONEST CARE</text>
  <text class="slab-light" x="283" y="275" font-size="100" textLength="429" lengthAdjust="spacingAndGlyphs">FOR ALL</text>
  <text class="slab-bold" x="285" y="311" font-size="30" textLength="425" lengthAdjust="spacingAndGlyphs">PATIENTS AND CLIENTS</text>

  <line class="rule" x1="270" y1="327" x2="722" y2="327"/>

  <!-- always -->
  <text class="slab-bold" x="287" y="355" font-size="11" textLength="32" lengthAdjust="spacingAndGlyphs">THIS</text>
  <text class="slab-bold" x="285" y="369" font-size="11" textLength="35" lengthAdjust="spacingAndGlyphs">MEANS</text>
  <text class="slab-light" x="327" y="373" font-size="42" textLength="383" lengthAdjust="spacingAndGlyphs">WE ARE <tspan class="initial">A</tspan>LWAYS</text>
  <text class="slab-light" x="284" y="440" font-size="78" textLength="427" lengthAdjust="spacingAndGlyphs">EFFICIENT</text>
  <text class="slab-bold" x="285" y="467" font-size="22" textLength="425" lengthAdjust="spacingAndGlyphs">WITH OUR RESOURCES TO PASS</text>
  <text class="condensed" x="285" y="503" font-size="42" textLength="425" lengthAdjust="spacingAndGlyphs">THE SAVINGS ON TO OUR CLIENTS</text>

  <line class="rule" x1="270" y1="517" x2="722" y2="517"/>

  <!-- ready / expanding -->
  <text class="slab-bold" x="285" y="551" font-size="27" textLength="425" lengthAdjust="spacingAndGlyphs">WE ARE ALSO <tspan class="initial">R</tspan>EADY TO HELP</text>
  <text class="condensed" x="285" y="596" font-size="46" textLength="425" lengthAdjust="spacingAndGlyphs">WITH THE BEST MEDICINE</text>
  <text class="slab-bold" x="285" y="635" font-size="43" textLength="280" lengthAdjust="spacingAndGlyphs">AVAILABLE</text>
  <text class="slab-bold" x="593" y="614" font-size="11" textLength="40" lengthAdjust="spacingAndGlyphs">WHILE</text>
  <text class="slab-bold" x="582" y="637" font-size="13" textLength="128" lengthAdjust="spacingAndGlyphs"><tspan class="initial" font-size="17">E</tspan>XPANDING</text>
  <text class="condensed" x="285" y="675" font-size="42" textLength="425" lengthAdjust="spacingAndGlyphs">TO HELP MORE OF OUR PRACTICE’S</text>
  <text class="slab-bold" x="285" y="706" font-size="30" textLength="425" lengthAdjust="spacingAndGlyphs">FAMILIES AND FARMS</text>

  <line class="rule" x1="270" y1="720" x2="722" y2="720"/>

  <!-- service -->
  <text class="slab-bold" x="285" y="752" font-size="23" textLength="425" lengthAdjust="spacingAndGlyphs">THIS IS HOW WE PROVIDE <tspan class="initial">S</tspan>ERVICE</text>
  <text class="slab-bold" x="285" y="774" font-size="22" textLength="425" lengthAdjust="spacingAndGlyphs">IN ABUNDANCE TO ALL OUR CLIENTS</text>
  <text class="slab-light" x="285" y="810" font-size="42" textLength="425" lengthAdjust="spacingAndGlyphs">SO THEY ARE PROUD</text>
  <text class="slab-bold" x="285" y="828" font-size="16" textLength="197" lengthAdjust="spacingAndGlyphs">TO SEND THEIR</text>
  <text class="slab-bold" x="285" y="843" font-size="11" textLength="197" lengthAdjust="spacingAndGlyphs">FAMILY AND FRIENDS</text>
  <text class="slab-light" x="490" y="847" font-size="42" textLength="220" lengthAdjust="spacingAndGlyphs">TO SEE US</text>

  <!-- footer ribbon -->
  <polygon class="band" points="272,857 720,857 706,877.5 720,898 272,898 286,877.5"/>
  <text class="slab-bold on-band" x="292" y="891" font-size="42" textLength="408" lengthAdjust="spacingAndGlyphs">BRINFORD VET CARES</text>
</svg>
</body>
</html>
```